Makeup Artist Requires Business Card design

Hi

I am looking for a business card design to market my makeup artist business. I operate under my own name Mara Veldt and I would like to keep the design of the card very simplistic and chic - something that keeps both my name and profession (makeup artist) the focus of the card. I would like it to be a style that is eyecatching to the reader (i am open to anything unusual) but upmarket.

Target Market(s)

women, magazine/beauty/fashion editors, photographers.

Industry/Entity Type

Business

Requirements
Must have
• Must contain:

Phone number: 0418 372 915
Website: www.maraveldt.com.au
email: contact@maraveldt.com.au

(although you don't need to have prefaced these with the words phone number, website etc :))
Should not have
• I am not looking for anything overly colorful - my preference is to keep the card dark if possible.

```html
<!DOCTYPE html>
<html lang="en">
<head>
<meta charset="utf-8">
<title>Business card presentation :: Mara Veldt - makeup artist</title>
<link rel="stylesheet" href="https://fonts.googleapis.com/css2?family=Jost:wght@400&family=Montserrat:wght@300;400&display=swap">
<style>
  :root {
    --sheet: #ffffff;
    --card: #353436;
    --card-ink: #ffffff;
    --sheet-ink: #555555;
    --portrait-light: #ffffff;
    --card-shadow: rgba(0, 0, 0, 0.35);
    --display-font: "Jost", sans-serif;
    --text-font: "Montserrat", sans-serif;
  }
  * { box-sizing: border-box; margin: 0; padding: 0; }
  html, body {
    width: 1200px;
    height: 849px;
    overflow: hidden;
    background: var(--sheet);
  }
  .sheet {
    position: relative;
    width: 1200px;
    height: 849px;
    font-family: var(--text-font);
    color: var(--sheet-ink);
  }
  .sheet-title {
    position: absolute;
    left: 72px;
    top: 69px;
    font-size: 18px;
    font-weight: 300;
    letter-spacing: 0.2px;
    white-space: nowrap;
  }
  .business-card {
    position: absolute;
    left: 317px;
    top: 194px;
    width: 565px;
    height: 332px;
    background: var(--card);
    box-shadow: 0 3px 10px var(--card-shadow);
    overflow: hidden;
    color: var(--card-ink);
  }
  .card-portrait {
    position: absolute;
    left: 0;
    top: 0;
    width: 165px;
    height: 290px;
  }
  .card-divider {
    position: absolute;
    left: 233px;
    top: 39px;
    width: 2px;
    height: 254px;
    background: var(--card-ink);
  }
  .card-name {
    position: absolute;
    left: 248px;
    top: 35px;
    font-family: var(--display-font);
    font-weight: 400;
    font-size: 66px;
    line-height: 60px;
    letter-spacing: 0.5px;
    text-transform: uppercase;
    white-space: nowrap;
  }
  .card-profession {
    position: absolute;
    left: 250px;
    top: 156px;
    font-weight: 400;
    font-size: 15px;
    letter-spacing: 8.6px;
    white-space: nowrap;
  }
  .card-contact {
    position: absolute;
    top: 228px;
    font-weight: 300;
    font-size: 17px;
    line-height: 23px;
    letter-spacing: 0.9px;
    list-style: none;
    white-space: nowrap;
  }
  .card-contact--labels { right: 346px; text-align: right; }
  .card-contact--values { left: 249px; }
  .spec-notes {
    position: absolute;
    left: 316px;
    top: 582px;
    font-size: 15px;
    font-weight: 300;
    line-height: 21.5px;
    list-style: none;
    white-space: nowrap;
  }
  .spec-notes li::before { content: "\2022\00a0"; }
</style>
</head>
<body>
<main class="sheet">
  <h1 class="sheet-title">business card presentation&nbsp; ::&nbsp; Mara Veldt - makeup artist</h1>

  <section class="business-card" aria-label="Business card front">
    <svg class="card-portrait" viewBox="0 0 165 290" role="img" aria-label="Stylised white portrait illustration of a made-up face in profile">
      <defs>
        <linearGradient id="portrait-tone" x1="0" y1="0" x2="1" y2="0">
          <stop offset="0" stop-color="var(--portrait-light)"/>
          <stop offset="0.6" stop-color="var(--portrait-light)"/>
          <stop offset="1" stop-color="var(--card)"/>
        </linearGradient>
      </defs>
      <rect width="165" height="290" fill="url(#portrait-tone)"/>
    </svg>

    <div class="card-divider"></div>
    <h2 class="card-name">Mara<br>Veldt</h2>
    <p class="card-profession">makeup&nbsp;&nbsp;&nbsp;&nbsp;artist</p>

    <ul class="card-contact card-contact--labels">
      <li>call</li>
      <li>web</li>
      <li>email</li>
    </ul>
    <ul class="card-contact card-contact--values">
      <li>0418 372 915</li>
      <li>www.maraveldt.com.au</li>
      <li>contact@maraveldt.com.au</li>
    </ul>
  </section>

  <ul class="spec-notes">
    <li>Colour - Grey (93% Black)</li>
    <li>Main font - Corvo Book</li>
    <li>Secondary font - Linden Sans (thin extended)</li>
  </ul>
</main>
</body>
</html>
```